Velmar Ops Business Cards

We need to design some upbeat business cards. We are an Industrial Rope Access Company/Height Safety Company that specialize in Rope Access, Confined Space, Anchor Points, Safety Systems, PPE Inspecions and Rigging.
Company name is Velmar Ops Ltd
Card is for Gareth Lomas the Company Director
His mobile number is 027 418 9072 and email is gareth@velmarops.co.nz. Website address is www.velmarops.co.nz.
We will post some pictures below to ensure you get a good idea of what we do.

```html
<!DOCTYPE html>
<html lang="en">
<head>
<meta charset="utf-8">
<title>Velmar Ops Ltd — Business Cards</title>
<link href="https://fonts.googleapis.com/css2?family=Open+Sans:wght@400;600;800&family=Roboto+Condensed:wght@300;400&display=swap" rel="stylesheet">
<style>
  :root {
    --page-bg: #e4e4e4;
    --card-bg: #221f20;
    --card-bg-light: #2c2829;
    --photo-dark: #1b1a1c;
    --photo-mid: #2f2d31;
    --accent-red: #c8473a;
    --text-main: #ffffff;
    --text-soft: #cfcfcf;
    --rule: #3a3637;
  }
  * { margin: 0; padding: 0; box-sizing: border-box; }
  html, body { width: 1200px; height: 1200px; overflow: hidden; }
  body {
    background: var(--page-bg);
    font-family: "Open Sans", Arial, sans-serif;
    display: flex;
    flex-direction: column;
    align-items: center;
    justify-content: center;
    gap: 60px;
  }
  .card {
    position: relative;
    width: 820px;
    height: 500px;
    background: var(--card-bg);
    overflow: hidden;
    box-shadow: 0 10px 24px rgba(0,0,0,0.25);
  }

  /* Front */
  .card--front {
    background: linear-gradient(160deg, var(--card-bg-light) 0%, var(--card-bg) 60%, #1c1a1b 100%);
  }
  .front-photo {
    position: absolute;
    left: 0; top: 0;
    width: 260px; height: 500px;
  }
  .front-logo {
    position: absolute;
    right: 70px; top: 70px;
    text-align: right;
    color: var(--text-main);
  }
  .wordmark {
    font-family: "Open Sans", Arial, sans-serif;
    font-weight: 800;
    font-size: 64px;
    line-height: 1;
    letter-spacing: 1px;
    color: var(--text-main);
  }
  .wordmark-suffix {
    display: block;
    font-weight: 600;
    font-size: 16px;
    margin-top: 4px;
  }
  .person {
    position: absolute;
    left: 300px; top: 230px;
  }
  .person-name {
    font-size: 30px;
    font-weight: 400;
    color: var(--text-main);
  }
  .person-role {
    font-size: 16px;
    color: var(--text-soft);
    margin-top: 2px;
  }
  .contacts {
    position: absolute;
    left: 300px; top: 340px;
    list-style: none;
  }
  .contacts li {
    display: flex;
    align-items: center;
    gap: 12px;
    font-size: 17px;
    color: var(--text-soft);
    height: 32px;
  }
  .contacts svg { width: 18px; height: 18px; fill: var(--text-main); }

  /* Back */
  .card--back {
    background: radial-gradient(ellipse at 70% 70%, #2e2a2b 0%, var(--card-bg) 55%, #1a1819 100%);
  }
  .back-photo {
    position: absolute;
    inset: 0;
  }
  .services {
    position: absolute;
    left: 90px; top: 50px;
    font-family: "Roboto Condensed", Arial, sans-serif;
    font-weight: 300;
    font-size: 22px;
    line-height: 1.35;
    color: var(--text-soft);
  }
  .services-title { text-transform: uppercase; }
  .back-logo {
    position: absolute;
    left: 150px; top: 250px;
  }
  .back-logo .wordmark { font-size: 92px; }
</style>
</head>
<body>

  <section class="card card--front" aria-label="Business card front">
    <svg class="front-photo" viewBox="0 0 260 500" role="img" aria-label="Photo of two rope access technicians in orange vests descending a dark building facade">
      <defs>
        <linearGradient id="facade" x1="0" y1="0" x2="1" y2="1">
          <stop offset="0" stop-color="#34323a"/>
          <stop offset="1" stop-color="#1b1a1d"/>
        </linearGradient>
      </defs>
      <rect width="260" height="500" fill="url(#facade)"/>
      <rect x="0" y="0" width="16" height="500" fill="var(--accent-red)" opacity="0.7"/>
    </svg>

    <div class="front-logo">
      <div class="wordmark">Velmar Ops<span class="wordmark-suffix">Ltd</span></div>
    </div>

    <div class="person">
      <div class="person-name">Gareth Lomas</div>
      <div class="person-role">Director</div>
    </div>

    <ul class="contacts">
      <li>
        <svg viewBox="0 0 24 24" aria-hidden="true"><path d="M6.6 10.8a15 15 0 0 0 6.6 6.6l2.2-2.2a1 1 0 0 1 1-.25 11.4 11.4 0 0 0 3.6.57 1 1 0 0 1 1 1V20a1 1 0 0 1-1 1A17 17 0 0 1 3 4a1 1 0 0 1 1-1h3.5a1 1 0 0 1 1 1c0 1.25.2 2.45.57 3.57a1 1 0 0 1-.25 1z"/></svg>
        027 418 9072
      </li>
      <li>
        <svg viewBox="0 0 24 24" aria-hidden="true"><circle cx="12" cy="12" r="10" fill="none" stroke="#fff" stroke-width="2"/><path d="M2 12h20M12 2c3 3 3 17 0 20M12 2c-3 3-3 17 0 20" fill="none" stroke="#fff" stroke-width="1.6"/></svg>
        www.velmarops.co.nz
      </li>
      <li>
        <svg viewBox="0 0 24 24" aria-hidden="true"><rect x="2" y="5" width="20" height="14" rx="1"/><path d="M2 5l10 8 10-8" fill="none" stroke="#222" stroke-width="1.8"/></svg>
        gareth@velmarops.co.nz
      </li>
    </ul>
  </section>

  <section class="card card--back" aria-label="Business card back">
    <svg class="back-photo" viewBox="0 0 820 500" preserveAspectRatio="none" role="img" aria-label="Faint dark photo of an industrial confined space interior">
      <defs>
        <radialGradient id="space" cx="0.72" cy="0.55" r="0.5">
          <stop offset="0" stop-color="#3a3536" stop-opacity="0.6"/>
          <stop offset="1" stop-color="#221f20" stop-opacity="0"/>
        </radialGradient>
      </defs>
      <rect width="820" height="500" fill="url(#space)"/>
    </svg>

    <div class="services">
      <div class="services-title">Specialize in</div>
      <div>Rope Access, Confined Space</div>
      <div>Anchor Points, Safety Systems</div>
      <div>PPE Inspecions &amp; Rigging</div>
    </div>

    <div class="back-logo">
      <div class="wordmark">Velmar Ops</div>
    </div>
  </section>

</body>
</html>
```